Freelance Makeup Artist Needing Business Card Design

I am a freelance makeup artist looking for a design for my business cards.
My target audience is people looking for bridal makeup, so i was thinking minimalistic style, black with white or gold foil accents.
Something that feels classy but simple and to the point.

I would like the front to state Marisa Pelworth and Makeup Artist, and the back to include my social media and contact details.

Target Market(s)

Brides, young women

Industry/Entity Type

Business

Contact Information for Business Card

0417352840
marisa.pelworth@quorvel.com
www.snapvale.com/marisa.pelworth
www.friendloop.com/MarisaPelworthMakeup

Requirements
Nice to have
• Social media icons next to relevant contact details

```html
<!DOCTYPE html>
<html lang="en">
<head>
<meta charset="utf-8">
<title>Marisa Pelworth – Makeup Artist Business Card</title>
<link rel="stylesheet" href="https://fonts.googleapis.com/css2?family=Montserrat:wght@200;300;400;500&display=swap">
<style>
  :root {
    --backdrop: #9a9a9a;
    --card-frame: #242424;
    --card-black: #030303;
    --band-grey: #232323;
    --ink-white: #ffffff;
    --ink-soft: #bdbdbd;
    --rule: #6a6a6a;
  }
  * { margin: 0; padding: 0; box-sizing: border-box; }
  html, body {
    width: 1200px; height: 1000px; overflow: hidden;
    background: var(--backdrop);
    font-family: "Montserrat", sans-serif;
  }
  .card {
    position: absolute; left: 301px; width: 600px; height: 350px;
  }
  .card-front { top: 124px; background: var(--card-frame); }
  .card-front .panel {
    position: absolute; left: 44px; top: 41px; width: 510px; height: 268px;
    background: var(--card-black);
    display: flex; flex-direction: column; align-items: center;
  }
  .monogram {
    font-weight: 300; font-size: 64px; letter-spacing: 4px; line-height: 1;
    color: var(--ink-white);
  }
  .card-front .monogram { margin-top: 42px; }
  .name {
    margin-top: 38px;
    font-weight: 400; font-size: 26px; letter-spacing: 2.5px;
    color: var(--ink-white); text-transform: uppercase;
  }
  .name-rule {
    width: 320px; height: 1px; background: var(--rule); margin-top: 8px;
  }
  .role {
    margin-top: 8px;
    font-weight: 300; font-size: 17px; letter-spacing: 4.5px;
    color: var(--ink-soft); text-transform: uppercase; word-spacing: 10px;
  }
  .card-back { top: 520px; background: var(--card-black); }
  .card-back .band {
    height: 192px; background: var(--band-grey);
    display: flex; justify-content: center; align-items: center;
  }
  .card-back .monogram { color: var(--card-black); font-weight: 500; }
  .contact {
    list-style: none; text-align: center; margin-top: 42px;
    font-size: 13px; line-height: 16.5px; color: var(--ink-white);
  }
</style>
</head>
<body>
  <section class="card card-front" aria-label="Card front">
    <div class="panel">
      <div class="monogram">MP</div>
      <h1 class="name">Marisa Pelworth</h1>
      <div class="name-rule"></div>
      <p class="role">Makeup Artist</p>
    </div>
  </section>

  <section class="card card-back" aria-label="Card back">
    <div class="band">
      <div class="monogram">MP</div>
    </div>
    <ul class="contact">
      <li>0417352840</li>
      <li>marisa.pelworth@quorvel.com</li>
      <li>www.snapvale.com/marisa.pelworth</li>
      <li>www.friendloop.com/MarisaPelworthMakeup</li>
    </ul>
  </section>
</body>
</html>
```